60 Ways to de-stress Poster

I would like a poster ( A4 full colour) with a list of 60 ways to destress. I would like the design to be clean and stylish (not cartoonish)

My Target market is stressed out mums so I want the poster to feel inspirational and relaxing to look at.

I have added a sample of something I like - but open to other ideas

Finished art would be print ready pdf

Target Market(s)

Mums who are stressed out - mainly new mums. I want this to be a poster that someone would happily put up that looks more like artwork.

Requirements
Must have
• My logo elements and colours but happy to incorporate other colours that blend well into it.

Colours:
Bright green: Pantone 376
Bright green as CMYK: c: 45.2% m: 0% y: 100% k: 0%

Logo text large grey: 70% black
Logo text strapline: 75% black
Tree: 80% black

Fonts:
Logo 'Willowbrook Calm': Verdana
Logo 'Counselling & coaching services for mums': Gill Sans Light
Should not have
• No cartoonish images - I want it very clean and stylish

```html
<!DOCTYPE html>
<html lang="en">
<head>
<meta charset="utf-8">
<title>60 Ways to De-stress</title>
<link href="https://fonts.googleapis.com/css2?family=Handlee&family=Noto+Sans:wght@600&family=Lato:wght@300&display=swap" rel="stylesheet">
<style>
  :root {
    --green: #8dc63f;
    --green-mid: #a9d46a;
    --green-light: #c8e39a;
    --green-pale: #e2f0c6;
    --cream: #f6f8d8;
    --logo-grey: #6d6e71;
    --strap-grey: #5f6062;
    --text: #333333;
    --bullet: #e0337a;
    --white: #ffffff;
  }
  * { margin: 0; padding: 0; box-sizing: border-box; }
  html, body { width: 849px; height: 1200px; overflow: hidden; background: var(--green); }
  .poster {
    position: relative;
    width: 849px; height: 1200px;
    background: var(--green);
  }
  .sheet {
    position: absolute;
    left: 32px; top: 32px;
    width: 786px; height: 1136px;
    background: var(--white);
    overflow: hidden;
  }
  .stripes { position: absolute; left: 0; top: 0; }
  .portrait {
    position: absolute;
    left: 190px; top: 20px;
    width: 280px; height: 450px;
    border-radius: 140px 140px 30px 30px;
    background: linear-gradient(180deg, #d9cfc7 0%, #8a7a72 35%, #5d7ea6 70%, #eae6e2 100%);
  }
  .brand {
    position: absolute;
    left: 468px; top: 108px;
    font-family: "Noto Sans", sans-serif;
  }
  .brand-name {
    font-weight: 600;
    font-size: 27px;
    color: var(--logo-grey);
    letter-spacing: -0.3px;
    display: flex; align-items: center; gap: 12px;
  }
  .brand-dot {
    width: 44px; height: 44px; border-radius: 50%;
    background: var(--logo-grey);
    margin-top: -40px;
  }
  .brand-strap {
    font-family: "Lato", sans-serif;
    font-weight: 300;
    font-size: 15.5px;
    color: var(--strap-grey);
  }
  .title {
    position: absolute;
    left: 33px; top: 488px;
    font-family: "Handlee", cursive;
    font-size: 73px;
    line-height: 80px;
    font-weight: 400;
    color: var(--green);
    white-space: nowrap;
  }
  .ways {
    position: absolute;
    top: 584px;
    list-style: none;
    font-family: "Handlee", cursive;
    font-size: 15px;
    color: var(--text);
  }
  .ways li {
    position: relative;
    height: 25.8px;
    line-height: 25.8px;
    padding-left: 16px;
    white-space: nowrap;
  }
  .ways li::before {
    content: "";
    position: absolute;
    left: 0; top: 11px;
    width: 5px; height: 5px; border-radius: 50%;
    background: var(--bullet);
  }
  .ways-one { left: 36px; }
  .ways-two { left: 261px; }
  .ways-three { left: 512px; }
  .corner { position: absolute; right: 0; bottom: 0; }
</style>
</head>
<body>
<div class="poster">
  <div class="sheet">
    <svg class="stripes" width="600" height="520" viewBox="0 0 600 520" aria-hidden="true">
      <polygon points="0,0 560,0 0,520" fill="var(--cream)"/>
      <polygon points="0,0 535,0 0,495" fill="var(--green-pale)"/>
      <polygon points="0,0 470,0 0,440" fill="var(--green-light)"/>
      <polygon points="0,0 400,0 0,370" fill="#b7db7f"/>
      <polygon points="0,0 330,0 0,300" fill="var(--green-mid)"/>
      <polygon points="0,0 250,0 0,230" fill="#9ccd55"/>
      <polygon points="0,0 160,0 0,150" fill="var(--green)"/>
    </svg>

    <div class="portrait" role="img" aria-label="Photograph of a smiling young mother sitting relaxed, hugging her knees, in a black top and jeans"></div>

    <div class="brand">
      <div class="brand-name">Willowbrook Calm <span class="brand-dot"></span></div>
      <div class="brand-strap">counselling &amp; coaching for mums</div>
    </div>

    <h1 class="title">60 Ways to De-stress</h1>

    <ul class="ways ways-one">
      <li>Put on some music and dance</li>
      <li>Make a gratitude list</li>
      <li>Eat something mindfully</li>
      <li>Go to the park</li>
      <li>Light a scented candle</li>
      <li>Buy yourself flowers</li>
      <li>Listening to music</li>
      <li>Call or visit a friend</li>
      <li>Take a nap</li>
      <li>Take some deep breaths</li>
      <li>Take a mini mental holiday</li>
      <li>Watch the clouds go by</li>
      <li>Have a bath</li>
      <li>Meditate</li>
      <li>Write in a journal</li>
      <li>Go for a walk</li>
      <li>Plant a tree</li>
      <li>Swing on a swing</li>
      <li>Forgive someone</li>
      <li>Write a poem</li>
    </ul>
    <ul class="ways ways-two">
      <li>Hug someone</li>
      <li>Fake a smile</li>
      <li>Gaze at the stars</li>
      <li>Play a game</li>
      <li>Stand up and stretch</li>
      <li>Paint a picture</li>
      <li>Read a book</li>
      <li>Look at a work of art</li>
      <li>Bake some cookies</li>
      <li>Go for a bike ride</li>
      <li>Review your achievements</li>
      <li>Relive happy memories</li>
      <li>Get a haircut</li>
      <li>Pat a dog</li>
      <li>Volunteer your time</li>
      <li>Perform an act of kindness</li>
      <li>Give yourself a time-out</li>
      <li>Make yourself a cup of tea</li>
      <li>Listen to a guided relaxation mp3</li>
      <li>Watch a funny movie</li>
    </ul>
    <ul class="ways ways-three">
      <li>Disconnect from technology</li>
      <li>Colour in</li>
      <li>Play in the Park</li>
      <li>Take a class at the gym</li>
      <li>Get a massage</li>
      <li>De-clutter a drawer</li>
      <li>Take a long drive</li>
      <li>Borrow a book from the library</li>
      <li>Go on a picnic</li>
      <li>Visit a farmers market</li>
      <li>Vent</li>
      <li>Live for today</li>
      <li>Ask for help</li>
      <li>Create some routines</li>
      <li>Scale down your to do list</li>
      <li>Accept what you can't change</li>
      <li>Compliment yourself often</li>
      <li>Outsource if you can</li>
      <li>Write positive self-statements</li>
      <li>Try Progressive Muscle Relaxation</li>
    </ul>

    <svg class="corner" width="100" height="90" viewBox="0 0 100 90" aria-hidden="true">
      <polygon points="100,0 100,90 0,90" fill="var(--cream)"/>
      <polygon points="100,25 100,90 30,90" fill="var(--green-pale)"/>
      <polygon points="100,50 100,90 58,90" fill="var(--green-light)"/>
      <polygon points="100,70 100,90 80,90" fill="var(--green-mid)"/>
    </svg>
  </div>
</div>
</body>
</html>
```